Bright Watt Partners
Simple
Carl Deming
President & CEO
31847 Tillery Lane
Fairmont Ridge, VA 20871
carld@brightwattpartners.com
www.brightwattpartners.com
Looking forward to seeing the results. Thanks, Carl
Here is the EPS file. Thanks

```html
<!DOCTYPE html>
<html lang="en">
<head>
<meta charset="utf-8">
<title>Bright Watt Partners – Stationery</title>
<link rel="stylesheet" href="https://fonts.googleapis.com/css2?family=Roboto:wght@400;700&display=swap">
<style>
  :root {
    --navy: #0b3f8f;
    --blue: #1262b8;
    --cyan: #27c4ea;
    --green: #7cc242;
    --lime: #a6d93b;
    --ink: #3a3a3a;
    --muted: #8a8a8a;
    --faint: #eef0f3;
    --paper: #ffffff;
    --shadow: rgba(0,0,0,0.18);
  }
  * { margin: 0; padding: 0; box-sizing: border-box; }
  html, body { width: 1200px; height: 737px; overflow: hidden; background: var(--paper); }
  body { position: relative; font-family: "Roboto", Arial, sans-serif; color: var(--ink); }

  .sheet { position: absolute; background: var(--paper); box-shadow: 0 1px 4px var(--shadow); overflow: hidden; }
  .sheet svg.swoosh { position: absolute; top: 0; left: 0; width: 100%; height: 100%; }

  .wordmark { position: absolute; font-weight: 700; color: var(--blue); white-space: nowrap; letter-spacing: -0.3px; }

  /* Letterhead */
  .letterhead { left: 19px; top: 14px; width: 421px; height: 686px; }
  .letterhead .wordmark { left: 26px; top: 46px; font-size: 24px; }
  .letterhead .watermark { position: absolute; left: 40px; top: 520px; font-size: 44px; font-weight: 700; color: var(--faint); transform: rotate(-32deg); transform-origin: left top; white-space: nowrap; }
  .letterhead .footer { position: absolute; left: 0; right: 0; bottom: 12px; text-align: center; font-size: 6.5px; color: var(--muted); white-space: nowrap; }

  /* Envelope */
  .envelope { left: 576px; top: 29px; width: 605px; height: 384px; }
  .envelope .wordmark { left: 34px; top: 192px; font-size: 27px; }
  .envelope .return { position: absolute; left: 36px; top: 230px; font-size: 7px; color: var(--muted); white-space: nowrap; }
  .envelope .watermark { position: absolute; right: 28px; top: 300px; font-size: 22px; font-weight: 700; color: var(--faint); transform: rotate(-28deg); white-space: nowrap; }

  /* Business cards */
  .card { width: 228px; height: 131px; }
  .card-front { left: 636px; top: 427px; }
  .card-back { left: 907px; top: 427px; }
  .card-green { left: 636px; top: 571px; background: radial-gradient(ellipse at 50% 45%, var(--lime) 0%, #5fae2e 70%, #3f8a22 100%); }
  .card-blue { left: 907px; top: 571px; background: radial-gradient(ellipse at 50% 45%, #2f8fd6 0%, var(--blue) 60%, var(--navy) 100%); }

  .card-front .wordmark { left: 12px; top: 20px; font-size: 12px; }
  .card-front .contact { position: absolute; left: 14px; top: 54px; font-size: 5.5px; line-height: 7.4px; color: var(--ink); white-space: nowrap; }
  .card-front .contact .name { font-size: 8px; font-weight: 700; color: var(--navy); line-height: 10px; }
  .card-front .contact .title { color: var(--muted); margin-bottom: 4px; }

  .card .centered { left: 50%; top: 50%; transform: translate(-50%, -50%); font-size: 13px; }
  .card-green .wordmark, .card-blue .wordmark { color: var(--paper); }
</style>
</head>
<body>

  <!-- Letterhead -->
  <section class="sheet letterhead">
    <svg class="swoosh" viewBox="0 0 421 686" preserveAspectRatio="none">
      <defs>
        <linearGradient id="lh-blue" x1="0" y1="0" x2="1" y2="0">
          <stop offset="0" stop-color="#2a9be0"/>
          <stop offset="1" stop-color="#0b3f8f"/>
        </linearGradient>
      </defs>
      <path d="M150 0 H421 V108 C340 60 250 26 150 0 Z" fill="url(#lh-blue)"/>
      <path d="M0 96 C120 70 290 70 421 114" fill="none" stroke="#7cc242" stroke-width="4"/>
      <path d="M0 104 C130 76 290 78 421 120" fill="none" stroke="#27c4ea" stroke-width="2"/>
    </svg>
    <div class="wordmark">Bright Watt Partners</div>
    <div class="watermark">Bright Watt Partners</div>
    <p class="footer">31847 Tillery Lane, Fairmont Ridge, VA 20871 | Toll free: 800-555-0190 | Phone: (301) 555-0148 | www.brightwattpartners.com</p>
  </section>

  <!-- Envelope -->
  <section class="sheet envelope">
    <svg class="swoosh" viewBox="0 0 605 384" preserveAspectRatio="none">
      <defs>
        <linearGradient id="env-blue" x1="0" y1="0" x2="1" y2="0">
          <stop offset="0" stop-color="#27c4ea"/>
          <stop offset="0.45" stop-color="#1a78cc"/>
          <stop offset="1" stop-color="#0b3f8f"/>
        </linearGradient>
      </defs>
      <path d="M0 0 H605 V236 C480 150 260 120 0 152 Z" fill="url(#env-blue)"/>
      <path d="M0 160 C260 128 480 158 605 244" fill="none" stroke="#7cc242" stroke-width="5"/>
      <rect x="0" y="376" width="605" height="8" fill="#0b3f8f"/>
    </svg>
    <div class="wordmark">Bright Watt Partners</div>
    <p class="return">31847 Tillery Lane | Fairmont Ridge, VA 20871</p>
    <div class="watermark">Bright Watt Partners</div>
  </section>

  <!-- Business card front -->
  <section class="sheet card card-front">
    <svg class="swoosh" viewBox="0 0 228 131" preserveAspectRatio="none">
      <defs>
        <linearGradient id="bc-blue" x1="0" y1="0" x2="1" y2="0">
          <stop offset="0" stop-color="#2a9be0"/>
          <stop offset="1" stop-color="#0b3f8f"/>
        </linearGradient>
      </defs>
      <path d="M60 0 H228 V131 H212 C212 70 160 18 60 0 Z" fill="url(#bc-blue)"/>
      <path d="M0 44 C100 30 190 60 206 131" fill="none" stroke="#7cc242" stroke-width="2.5"/>
    </svg>
    <div class="wordmark">Bright Watt Partners</div>
    <div class="contact">
      <div class="name">Carl Deming</div>
      <div class="title">President &amp; CEO</div>
      <div>31847 Tillery Lane, Fairmont Ridge, VA 20871</div>
      <div>Toll free: 800-555-0190 | Phone: (301) 555-0148</div>
      <div>Cell: (301) 555-0172</div>
      <div>carld@brightwattpartners.com</div>
      <div>www.brightwattpartners.com</div>
    </div>
  </section>

  <!-- Business card back -->
  <section class="sheet card card-back">
    <div class="wordmark centered">Bright Watt Partners</div>
  </section>

  <!-- Green variant -->
  <section class="sheet card card-green">
    <div class="wordmark centered">Bright Watt Partners</div>
  </section>

  <!-- Blue variant -->
  <section class="sheet card card-blue">
    <div class="wordmark centered">Bright Watt Partners</div>
  </section>

</body>
</html>
```